Industrial Recycling

-We are a recycling company. this postcard will be sent to industrial businesses. The name of our company is Grainfield Salvage Partners. We want these businesses to contact us so that we can purchase their recyclable materials from them. We want to target Scrap Metal, Cardboard, Plastic, Waste Paper, Food Waste, Bakery Waste, E-Waste, Solid Fill. I want the Headline to be- We have been recycling for over 100 years. Under or over the headline, I want the attached picture. My attached picture will be the dominant picture. I also want a couple of other pictures: some ideas are- baled cardboard, baled scrap metal, Money, loose recyclables. anything else that looks good to you! A tagline will be: Our specialty is recycling unique waste-streams. another tagline will be: If a waste can be recycled, we will find a use for it! Another tagline: All it takes is one call or email, and we will handle the rest. Please include the attached logo.- Please include the following contact info:
Phone number is 800-274-5196, email is ned@salvo728.com, website is salvo728.com.

Good Morning, We would like to make a couple more changes to the post card before we chose a design. We are sorry for such a late request. Please remove the tag lines; If a waste can be recycled, we will find a use for it! And: All it takes is one call or email, and we will handle the rest. Please replace these tag lines with: "Call or email to schedule your free waste audit" and please remember to list: “Scrap Metal, Cardboard, Plastic, Waste Paper, Food Waste, Bakery Waste, E-Waste, Solid Fill” as some of the recyclable material we are looking to buy.

```html
<!DOCTYPE html>
<html lang="en">
<head>
<meta charset="utf-8">
<title>Grainfield Salvage Partners – Postcard</title>
<link rel="stylesheet" href="https://fonts.googleapis.com/css2?family=Questrial&family=Montserrat:wght@600;700&family=Arimo:ital,wght@0,700;1,700&family=Kalam:wght@300&display=swap">
<style>
  :root {
    --stage: #424242;
    --paper: #ffffff;
    --green: #79a05a;
    --charcoal: #4f4d4a;
    --ink: #0c0c0c;
    --rule: #9a9a9a;
    --sepia-light: #c9b9a2;
    --sepia-dark: #6e5f4d;
  }
  * { box-sizing: border-box; margin: 0; padding: 0; }
  html, body {
    width: 1029px; height: 1200px; overflow: hidden;
    background: var(--stage);
    font-family: "Questrial", "Century Gothic", sans-serif;
  }
  .card { position: absolute; background: var(--paper); overflow: hidden; }
  .card--front { left: 73px; top: 21px; width: 876px; height: 567px; }
  .card--back  { left: 75px; top: 609px; width: 875px; height: 565px; }

  .front-top-shade {
    position: absolute; left: 0; top: 0; width: 100%; height: 190px;
    background: linear-gradient(#eeeeee, #ffffff 45%);
  }
  .front-wave { position: absolute; left: 0; top: 0; }

  .brand {
    position: absolute; display: flex; align-items: center; gap: 12px;
    font-family: "Montserrat", sans-serif; font-weight: 700;
    color: var(--charcoal); white-space: nowrap;
  }
  .brand__mark { width: 32px; height: 32px; background: var(--green); flex: none; }
  .card--front .brand { left: 36px; top: 52px; font-size: 22px; }
  .card--back .brand { left: 108px; top: 44px; font-size: 25px; }
  .card--back .brand__mark { width: 36px; height: 36px; }

  .headline {
    position: absolute; left: 410px; top: 44px; width: 440px; height: 100px;
    color: var(--charcoal); line-height: 1; font-weight: 400;
  }
  .headline span { position: absolute; white-space: nowrap; }
  .headline__lead { left: 87px; top: 0; font-size: 34px; }
  .headline__main { left: 0; top: 34px; font-size: 33px; }
  .headline__main strong {
    font-family: "Montserrat", sans-serif; font-weight: 700; font-size: 31px;
  }
  .headline__years-num {
    left: 308px; top: 4px;
    font-family: "Kalam", cursive; font-weight: 300; font-style: italic;
    font-size: 68px; color: var(--green); letter-spacing: 5px;
  }
  .headline__years { left: 332px; top: 58px; font-size: 38px; }

  .hero-photo {
    position: absolute; left: 39px; top: 117px; width: 448px; height: 205px;
    border: 3px solid var(--paper);
    background: linear-gradient(160deg, var(--sepia-light), #a8967d 55%, var(--sepia-dark));
  }

  .audit-call { position: absolute; left: 0; top: 0; width: 100%; height: 340px; color: var(--paper); }
  .audit-call span { position: absolute; white-space: nowrap; line-height: 1; }
  .audit-call__l1 { left: 508px; top: 196px; font-size: 39px; }
  .audit-call__l2 { left: 530px; top: 236px; font-size: 32px; }
  .audit-call__l3 { left: 622px; top: 270px; font-size: 32px; }
  .audit-call__free {
    left: 705px; top: 256px;
    font-family: "Arimo", sans-serif; font-weight: 700; font-size: 50px;
  }
  .audit-call__l4 { left: 561px; top: 302px; font-size: 32px; }

  .material-circle {
    position: absolute; top: 345px; width: 120px; height: 120px; border-radius: 50%;
    border: 3px solid #e9e9e9; box-shadow: 0 4px 6px rgba(0,0,0,.3);
  }
  .material-circle--metal { left: 497px; background: radial-gradient(circle at 40% 35%, #8d7a66, #4c3b2f 70%); }
  .material-circle--money { left: 610px; background: radial-gradient(circle at 45% 40%, #cfd6c4, #7f8d77 75%); }
  .material-circle--cardboard { left: 726px; background: radial-gradient(circle at 50% 40%, #c59a74, #8a6446 75%); }

  .specialty {
    position: absolute; left: 39px; top: 348px; width: 450px;
    font-family: "Arimo", sans-serif; font-weight: 700; font-style: italic;
    font-size: 21px; line-height: 1.12; color: var(--ink); text-transform: uppercase;
  }
  .materials {
    position: absolute; left: 39px; width: 450px;
    list-style: none; display: flex; gap: 12px;
    font-family: "Arimo", sans-serif; font-weight: 700; font-size: 16px; color: var(--paper);
  }
  .materials--row1 { top: 404px; }
  .materials--row2 { top: 427px; }
  .materials li { white-space: nowrap; }
  .materials li::before {
    content: ""; display: inline-block; width: 5px; height: 5px;
    background: var(--ink); margin-right: 3px; vertical-align: 3px;
  }

  .contact-bar {
    position: absolute; left: 0; top: 477px; width: 100%; height: 90px; background: var(--ink);
  }
  .contact-phone {
    position: absolute; left: 45px; top: 12px; display: flex; align-items: center; gap: 10px;
    font-family: "Montserrat", sans-serif; font-weight: 700; font-size: 52px; color: var(--green);
    white-space: nowrap; line-height: 1.2;
  }
  .contact-online {
    position: absolute; left: 545px; top: 8px; list-style: none;
    color: var(--paper); font-size: 28px; line-height: 30px; letter-spacing: .5px;
  }
  .contact-online li { display: flex; align-items: center; gap: 8px; white-space: nowrap; }

  .return-address {
    position: absolute; left: 109px; top: 111px;
    font-family: "Montserrat", sans-serif; font-weight: 600; font-size: 16.5px;
    color: var(--charcoal); white-space: nowrap;
  }
  .stamp-box {
    position: absolute; left: 757px; top: 38px; width: 75px; height: 85px;
    border: 1px solid #b5b5b5; padding: 20px 0 0 18px;
    font-size: 14px; line-height: 17px; color: #8c8c8c;
  }
  .back-green { position: absolute; left: 0; top: 153px; width: 581px; height: 250px; background: var(--green); }
  .back-black-upper { position: absolute; left: 0; top: 403px; width: 581px; height: 86px; background: var(--ink); }
  .back-black-lower { position: absolute; left: 0; top: 489px; width: 377px; height: 76px; background: var(--ink); }
  .address-line { position: absolute; left: 611px; width: 234px; height: 1px; background: var(--rule); }
</style>
</head>
<body>

<section class="card card--front">
  <div class="front-top-shade"></div>
  <svg class="front-wave" width="876" height="567" viewBox="0 0 876 567" aria-hidden="true">
    <path d="M0 198 Q 420 120 876 163 L876 184 Q 420 145 0 222 Z" fill="#0c0c0c"/>
    <path d="M0 222 Q 420 145 876 184 L876 477 L0 477 Z" fill="#79a05a"/>
  </svg>

  <div class="brand"><span class="brand__mark"></span>Grainfield Salvage Partners</div>

  <h1 class="headline">
    <span class="headline__lead">We have been</span>
    <span class="headline__main"><strong>RECYCLING</strong> for over</span>
    <span class="headline__years-num">100</span>
    <span class="headline__years">years</span>
  </h1>

  <div class="hero-photo" role="img" aria-label="Vintage sepia photo of two workers beside an early open-bed salvage truck"></div>

  <p class="audit-call">
    <span class="audit-call__l1">Call or Email</span>
    <span class="audit-call__l2">To Schedule</span>
    <span class="audit-call__l3">Your</span>
    <span class="audit-call__free">FREE</span>
    <span class="audit-call__l4">Waste Audit</span>
  </p>

  <div class="material-circle material-circle--metal" role="img" aria-label="Pile of scrap metal"></div>
  <div class="material-circle material-circle--money" role="img" aria-label="Scattered banknotes"></div>
  <div class="material-circle material-circle--cardboard" role="img" aria-label="Stacked bales of cardboard"></div>

  <p class="specialty">Our specialty is recycling unique<br>waste-streams, as well as:</p>
  <ul class="materials materials--row1">
    <li>Scrap Metal</li><li>Cardboard</li><li>Plastic</li><li>Waste Paper</li>
  </ul>
  <ul class="materials materials--row2">
    <li>Food Waste</li><li>Bakery Waste</li><li>E-Waste</li><li>Solid Fill etc</li>
  </ul>

  <div class="contact-bar">
    <div class="contact-phone">
      <svg width="42" height="42" viewBox="0 0 40 40" aria-hidden="true">
        <circle cx="20" cy="20" r="18" fill="none" stroke="#fff" stroke-width="2.5"/>
        <path d="M14 10 l4 0 l2 6 l-3 2 q2 5 6 7 l2 -3 l6 2 l0 4 q-1 2 -4 2 q-15 -3 -15 -17 q0 -3 2 -3 z" fill="none" stroke="#fff" stroke-width="2" stroke-linejoin="round"/>
      </svg>
      800 - 274-5196
    </div>
    <ul class="contact-online">
      <li>
        <svg width="24" height="24" viewBox="0 0 22 22" aria-hidden="true" fill="none" stroke="#fff" stroke-width="1.5">
          <circle cx="11" cy="11" r="9"/><ellipse cx="11" cy="11" rx="4" ry="9"/>
          <path d="M2 11h18M4 6h14M4 16h14"/>
        </svg>
        www.salvo728.com
      </li>
      <li>
        <svg width="26" height="19" viewBox="0 0 24 18" aria-hidden="true" fill="none" stroke="#fff" stroke-width="1.5">
          <rect x="1" y="2" width="22" height="14"/><path d="M1 2l11 8 11-8M1 16l8-7M23 16l-8-7"/>
        </svg>
        Ned@salvo728.com
      </li>
    </ul>
  </div>
</section>

<section class="card card--back">
  <div class="brand"><span class="brand__mark"></span>Grainfield Salvage Partners</div>
  <p class="return-address">1874 HARLOW AVE ALDER BAY, CA 90418</p>
  <div class="stamp-box">Place<br>Stamp<br>Here</div>
  <div class="back-green"></div>
  <div class="back-black-upper"></div>
  <div class="back-black-lower"></div>
  <div class="address-line" style="top:354px"></div>
  <div class="address-line" style="top:400px"></div>
  <div class="address-line" style="top:448px"></div>
</section>

</body>
</html>
```